Electrical Contracting Business Website

Require website done for my contracting business.
Partly done one but really dont have time.

You can view the current one at http://brelton.net.au

You can use any info/styles/photos from the current website

I like the orange color of the logo so id like things to be with that
Unfortunatly being a new business (Sept 2015) I havent got alot of photos . but if you require any for any of the specifics listed in the doc file ill have a look to see what I have.

I am targeting mainly commercial / industrial clients. Which also includes government and mining.

Target Market(s)

People requiring electricians

Industry/Entity Type

Electrician

Coding

Number of Pages Required

Colors
f37122

Requirements
Must have
• logo with EC Number
• Keep it simple and not to complicated
• Comply with the current html / style sheet standards.
• Desktop/Mobile Version compatability
Nice to have
• additional photos.
• The domestic lifts we install are by vostrel I dont have any photos of them unfortunately.
Should not have
• change colour of logo

```html
<!DOCTYPE html>
<html lang="en">
<head>
<meta charset="utf-8">
<title>Brelton Engineering – Electrical Services</title>
<link rel="stylesheet" href="https://fonts.googleapis.com/css2?family=Open+Sans:wght@400;600;700;800&display=swap">
<style>
:root{
  --orange:#f37122;
  --ink:#222;
  --text:#444;
  --muted:#666;
  --light:#f5f5f5;
  --line:#d6d6d6;
  --footer:#1c1c1c;
  --footer-deep:#0d0d0d;
  --white:#fff;
}
*{box-sizing:border-box;margin:0;padding:0}
html,body{width:1200px;height:2902px;overflow:hidden}
body{font-family:'Open Sans',Arial,sans-serif;color:var(--text);background:var(--white);position:relative}
.abs{position:absolute}
a{color:inherit;text-decoration:none}

/* top nav */
.topbar{position:absolute;left:0;top:0;width:1200px;height:44px;background:var(--orange);color:var(--white)}
.topbar .menu{position:absolute;left:101px;top:0;height:44px;display:flex;align-items:center;gap:32px;font-size:14px}
.topbar .menu svg{display:block}
.topbar .socials{position:absolute;right:100px;top:7px;display:flex;gap:10px}
.topbar .socials span{width:30px;height:30px;border-radius:50%;border:2px solid rgba(255,255,255,.7);background:rgba(255,255,255,.15)}

/* header */
.header{position:absolute;left:0;top:44px;width:1200px;height:110px;background:var(--white)}
.header .reg{position:absolute;left:101px;top:30px;font-size:12px;line-height:18px;color:var(--ink)}
.header .reg b{font-weight:700}
.brand{position:absolute;left:500px;top:30px;width:200px;display:flex;align-items:center;justify-content:center;gap:10px;color:var(--orange);font-weight:800;font-size:30px;letter-spacing:1px}
.brand i{width:22px;height:22px;border-radius:50%;background:var(--orange);display:block}
.header .call{position:absolute;right:99px;top:38px;display:flex;gap:10px;align-items:center;color:var(--ink)}
.header .call div{font-size:14px;line-height:19px}
.header .call b{font-weight:700}

/* hero */
.hero{position:absolute;left:0;top:154px;width:1200px;height:518px;background:linear-gradient(100deg,#6d6e6a 0%,#8f8c82 40%,#5c5a55 70%,#3c3f48 100%)}
.hero h1{position:absolute;left:210px;top:200px;font-size:36px;line-height:44px;font-weight:700;color:var(--white)}
.hero .arrow{position:absolute;top:205px}

/* section heads */
.sec-title{position:absolute;left:0;width:1200px;text-align:center;font-size:28px;font-weight:700;color:var(--ink)}
.sec-title span,.about h2 span{color:var(--orange)}
.divider{position:absolute;left:425px;width:350px;height:14px}
.lead{position:absolute;left:110px;width:980px;text-align:center;font-size:15px;line-height:26px;color:var(--text)}

/* services */
.band{position:absolute;left:0;top:1049px;width:1200px;height:180px;background:var(--orange)}
.card{position:absolute;top:873px;width:318px}
.card .photo{width:318px;height:250px;border:7px solid var(--white);box-shadow:0 1px 6px rgba(0,0,0,.25)}
.card h3{margin-top:20px;text-align:center;color:var(--white);font-size:21px;font-weight:700}
.card p{text-align:center;color:var(--white);font-size:12px;line-height:19px;margin-top:2px}

/* about */
.about h2{position:absolute;left:101px;top:1264px;font-size:28px;font-weight:700;color:var(--ink)}
.about .sub{position:absolute;left:101px;top:1340px;font-size:16px;font-weight:600;color:var(--orange)}
.about p{position:absolute;left:101px;width:640px;font-size:12.5px;line-height:24px;color:var(--text)}
.btn{position:absolute;background:var(--orange);color:var(--white);font-size:13px;display:flex;align-items:center;justify-content:center;border-radius:2px}
.values{position:absolute;left:794px;top:1272px;width:308px;height:308px;background:radial-gradient(circle at 50% 50%,#ffffff 0%,#ffffff 30%,#f8b58c 55%,#f37122 100%);border-radius:6px}

/* gallery */
.gallery{position:absolute;left:0;top:1623px;width:1200px;height:687px;background:var(--light)}
.shot{position:absolute}

/* contact */
.contact{position:absolute;left:0;top:2310px;width:1200px;height:268px;background:linear-gradient(90deg,#fff 0%,#fbfbfb 60%,#f1f1f1 100%)}
.contact h2{position:absolute;left:101px;top:44px;font-size:31px;line-height:40px;font-weight:700;color:var(--orange)}
.contact p{position:absolute;left:101px;top:140px;width:300px;font-size:13px;line-height:22px;color:var(--muted)}
.field{position:absolute;width:310px;height:44px;background:var(--white);border:1px solid var(--line);font-size:13px;color:var(--text);padding:13px 14px}

/* footer */
.footer{position:absolute;left:0;top:2578px;width:1200px;height:279px;background:var(--footer);color:#ccc}
.footer h4{position:absolute;top:40px;font-size:18px;font-weight:600;color:var(--white)}
.footer ul{position:absolute;left:101px;top:78px;list-style:none;font-size:13px;line-height:26px;color:#ddd}
.footer li::before{content:"›";margin-right:14px;font-weight:700}
.footer .info{position:absolute;left:300px;top:78px;font-size:13px;line-height:21px;color:#bbb}
.footer .fsoc{position:absolute;left:300px;top:218px;display:flex;gap:10px}
.footer .fsoc span{width:26px;height:26px;background:#2a6ebb;border-radius:2px}
.map{position:absolute;left:538px;top:44px;width:284px;height:154px;background:linear-gradient(135deg,#dfe7ee 0%,#c9d8e6 50%,#e8ecde 100%)}
.footer .viewmap{position:absolute;left:540px;top:210px;font-size:13px;color:var(--orange);text-decoration:underline}
.fbrand{position:absolute;left:922px;top:60px;display:flex;align-items:center;gap:10px;color:#ddd;font-weight:800;font-size:26px;letter-spacing:1px}
.fbrand i{width:20px;height:20px;border-radius:50%;background:#ddd;display:block}
.badge{position:absolute;left:932px;top:140px;width:150px;height:60px;border-radius:4px;background:#3a3a3a}
.copy{position:absolute;left:0;top:2857px;width:1200px;height:45px;background:var(--footer-deep);color:#ddd;font-size:13px;display:flex;align-items:center;justify-content:center}
</style>
</head>
<body>

<nav class="topbar">
  <div class="menu">
    <svg width="18" height="16" viewBox="0 0 18 16"><path d="M9 1 1 8h2.5v7h4v-4.5h3V15h4V8H17z" fill="#fff"/></svg>
    <a>About Us</a><a>Residential ▾</a><a>Commercial ▾</a><a>Industrial ▾</a><a>Project Gallery</a><a>Contact Us</a>
  </div>
  <div class="socials"><span></span><span></span><span></span><span></span></div>
</nav>

<header class="header">
  <div class="reg"><b>ACN :</b> 600 214 905<br><b>ABN :</b> 41 305 728 116<br><b>EC LIC :</b> 10473</div>
  <div class="brand"><i></i>BRELTON</div>
  <div class="call">
    <svg width="24" height="24" viewBox="0 0 24 24"><path d="M6.6 10.8a15 15 0 0 0 6.6 6.6l2.2-2.2c.3-.3.7-.4 1-.2 1.1.4 2.3.6 3.6.6.6 0 1 .4 1 1V20c0 .6-.4 1-1 1A17 17 0 0 1 3 4c0-.6.4-1 1-1h3.5c.6 0 1 .4 1 1 0 1.3.2 2.5.6 3.6.1.3 0 .7-.2 1z" fill="#f37122"/></svg>
    <div><b>Call Us Today</b><br>0400 123 456</div>
  </div>
</header>

<section class="hero" role="img" aria-label="Electrician soldering a circuit board at a workbench">
  <h1>we are specialized in<br>electrical services</h1>
  <svg class="arrow" style="left:30px" width="40" height="80" viewBox="0 0 40 80"><path d="M36 4 4 40l32 36" fill="none" stroke="#fff" stroke-width="3"/></svg>
  <svg class="arrow" style="left:1130px" width="40" height="80" viewBox="0 0 40 80"><path d="M4 4l32 36L4 76" fill="none" stroke="#fff" stroke-width="3"/></svg>
</section>

<h2 class="sec-title" style="top:710px">Our <span>Services</span></h2>
<svg class="divider" style="top:762px" viewBox="0 0 350 14"><line x1="0" y1="10" x2="350" y2="10" stroke="#ccc"/><circle cx="175" cy="7" r="6" fill="#ccc"/></svg>
<p class="lead" style="top:792px">in hendrerit in vulputate velit esse molestie consequat, vel illum dolore eu feugiat nulla facilisis at vero eros et accumsan et iusto odio dignissim qui blandit praesent luptatum zzril delenit augue duis dolore te feugait nulla facilisi.</p>
<div class="band"></div>
<div class="card" style="left:101px">
  <div class="photo" role="img" aria-label="Electrician working on a residential switchboard" style="background:linear-gradient(135deg,#9aa2a6,#c9c6bc 60%,#7b8084)"></div>
  <h3>Residential Work</h3>
  <p>Lorem ipsum dolor smit amet, consectetuer<br>adipiscing elitmk, sed amet diam ...</p>
</div>
<div class="card" style="left:441px">
  <div class="photo" role="img" aria-label="Power transmission towers against a sunset sky" style="background:linear-gradient(180deg,#3a6fa8 0%,#7a86a0 45%,#e39a3c 75%,#3d2a1d 100%)"></div>
  <h3>Commercial Work</h3>
  <p>Lorem ipsum dolor smit amet, consectetuer<br>adipiscing elitmk, sed amet diam ...</p>
</div>
<div class="card" style="left:783px">
  <div class="photo" role="img" aria-label="Technician beside a server rack in a data room" style="background:linear-gradient(135deg,#4a5a70,#9eb3c8 55%,#d8e2ec)"></div>
  <h3>Industrial work</h3>
  <p>Lorem ipsum dolor smit amet, consectetuer<br>adipiscing elitmk, sed amet diam ...</p>
</div>

<section class="about">
  <h2>About <span>Brelton Engineering</span></h2>
  <svg class="abs" style="left:101px;top:1314px" width="16" height="16" viewBox="0 0 16 16"><circle cx="8" cy="8" r="7" fill="#ddd"/></svg>
  <div class="sub">Lorem ipsum dolor sit amet, consectetuer adipiscing elit</div>
  <p style="top:1374px">nibh euismod tincidunt ut laoreet dolore magna aliquam erat volutpat. Ut wisi enim ad min im veniam, quis nostrud exerci tation ullamcorper suscipit lobortis nisl ut aliquip ex ea com modo consequat. Duis autem vel eum iriure dolor.</p>
  <p style="top:1456px">In hendrerit in vulputate velit esse molestie consequat, vel illum dolore eu feugiat nulla facilisis at vero eros et accumsan et iusto odio dignissim qui blandit praesent luptatum zzril delenit augue duis dolore te feugait nulla facilisi.</p>
  <div class="btn" style="left:101px;top:1543px;width:122px;height:36px">Read More »</div>
  <div class="values" role="img" aria-label="Four orange gear badges for satisfaction guarantee, safety, quality and reliability joined around the company name"></div>
</section>

<section class="gallery">
  <h2 class="sec-title" style="top:28px">Recent <span>Project Gallery</span></h2>
  <svg class="divider" style="top:80px" viewBox="0 0 350 14"><line x1="0" y1="10" x2="350" y2="10" stroke="#ccc"/><circle cx="175" cy="7" r="6" fill="#ccc"/></svg>
  <p class="lead" style="top:110px">in hendrerit in vulputate velit esse molestie consequat, vel illum dolore eu feugiat nulla facilisis at vero eros et accumsan et iusto odio dignissim qui blandit praesent luptatum zzril delenit augue duis dolore te feugait nulla facilisi.</p>
  <div class="shot" role="img" aria-label="Hand stripping blue and brown wires with pliers" style="left:101px;top:196px;width:434px;height:386px;background:linear-gradient(135deg,#d9dde2,#c7a48d 50%,#3d6fb0)"></div>
  <div class="shot" role="img" aria-label="Industrial motors and pipework" style="left:564px;top:196px;width:256px;height:180px;background:linear-gradient(135deg,#3b3d3f,#7c8186 60%,#2a2b2d)"></div>
  <div class="shot" role="img" aria-label="Digital meter on a red panel" style="left:845px;top:196px;width:256px;height:180px;background:linear-gradient(135deg,#c8281f,#7a1c17 60%,#3c3f2a)"></div>
  <div class="shot" role="img" aria-label="Circuit breakers in a distribution board" style="left:564px;top:402px;width:256px;height:180px;background:linear-gradient(135deg,#e7e7e2,#a9aca8 60%,#555)"></div>
  <div class="shot" role="img" aria-label="Wired control board inside an orange enclosure" style="left:845px;top:402px;width:256px;height:180px;background:linear-gradient(135deg,#d7841f,#8a4a12 60%,#3a2a18)"></div>
  <div class="btn" style="left:538px;top:611px;width:124px;height:34px">View All »</div>
</section>

<section class="contact">
  <h2>Any Questions you<br>would like to ask?</h2>
  <p>Duis autem vel eum iriure dolormi opl inmoklimort hendi rerit in vulpu tatemil velitm essemol monop molestiel conseqh uat, velmi illum dolor eokf lla more facilisis... [+]</p>
  <div class="field" style="left:456px;top:70px">Name</div>
  <div class="field" style="left:790px;top:70px">Email</div>
  <div class="field" style="left:456px;top:123px">Phone</div>
  <div class="field" style="left:790px;top:123px">Message</div>
  <div class="btn" style="left:456px;top:176px;width:126px;height:36px">SUBMIT »</div>
</section>

<footer class="footer">
  <h4 style="left:101px">Quick Link</h4>
  <ul><li>Home</li><li>About Us</li><li>Residential</li><li>Commercial</li><li>Industrial</li><li>Project Gallery</li><li>Contact Us</li></ul>
  <h4 style="left:300px">Contact Detail</h4>
  <div class="info">Maple Rise, Western<br>Australia, 6100.<br><br>Phone : 0400 123 456<br>Fax : 08 6100 4400<br>Email : info@brelton.net.au</div>
  <div class="fsoc"><span></span><span></span><span></span></div>
  <div class="map" role="img" aria-label="Street map showing the office location"></div>
  <a class="viewmap">View Map</a>
  <div class="fbrand"><i></i>BRELTON</div>
  <div class="badge"></div>
</footer>
<div class="copy">Copyright © 2016 brelton &nbsp;All Right Reserved.</div>

</body>
</html>
```